Venture capital website it shall be called Talvo Ventures

Venture capital Name is : Talvo Ventures

i have already regesieted a website and comunicate the details with you when i choose a design.

i need a simple website design for a newly established venture capital. i would like something similar to the websites listed down:

http://www.quillmarsh.com/

http://www.derobrightventures.com/

https://kplorin.com/

http://www.vintelhold.com/

i like vintel hold the most

Target Market(s)

entrepreneur - startups

Industry/Entity Type

Venture Capital

Number of Pages Required

4 page

Font styles to use
Serif
Sans Serif

Colors
ffc214
fece3e

Requirements
Must have
• the following sections:
• Philosophy (about talvo Ventures)
• Team
• Knowledge
• address - contact
Nice to have
• http://www.quillmarsh.com/
• http://www.derobrightventures.com/
• https://kplorin.com/
• http://www.vintelhold.com/

```html
<!DOCTYPE html>
<html lang="en">
<head>
<meta charset="utf-8">
<title>Talvo Ventures</title>
<link href="https://fonts.googleapis.com/css2?family=Montserrat:wght@400;600;700;800&display=swap" rel="stylesheet">
<style>
  :root{
    --stage:#272727;
    --ink:#1a1a1a;
    --black:#111111;
    --gold:#b59e32;
    --pale:#ede5cc;
    --white:#ffffff;
  }
  *{margin:0;padding:0;box-sizing:border-box}
  html,body{width:1200px;height:1200px;overflow:hidden;background:var(--stage)}
  body{font-family:'Montserrat',sans-serif;color:var(--ink)}
  .site{position:absolute;left:70px;top:107px;width:1062px;height:986px;background:var(--white);overflow:hidden}
  .shapes{position:absolute;left:0;top:0;width:1062px;height:986px}
  .abs{position:absolute}

  .brand{left:22px;top:20px;display:flex;align-items:center;gap:9px;color:var(--white)}
  .brand-mark{width:9px;height:9px;background:var(--gold)}
  .brand-name{font-size:26px;font-weight:700;letter-spacing:4px;line-height:1}

  .nav{top:22px;right:38px;display:flex;gap:24px;list-style:none}
  .nav li{color:var(--white);font-size:12.5px;font-weight:600}
  .nav li:first-child{font-weight:700}

  .hero-title{left:124px;top:188px;font-size:38px;font-weight:800;color:var(--gold);letter-spacing:-.3px;line-height:1.2}
  .hero-sub{left:124px;top:237px;font-size:18px;font-weight:400}
  .hero-copy{left:124px;top:267px;width:404px;font-size:10.2px;line-height:16.6px;color:#333}
  .btn{left:125px;top:351px;width:92px;height:28px;background:var(--gold);color:var(--white);font-size:10px;display:flex;align-items:center;justify-content:center}

  .member-copy{width:320px;font-size:10.2px;line-height:16.6px;color:var(--white)}
  .member-name{font-size:13.5px;font-weight:700;color:var(--white)}
  .member-left .member-copy{left:64px;top:585px;width:318px}
  .member-left .member-name{left:65px;top:717px}
  .member-right .member-name{right:46px;top:585px}
  .member-right .member-copy{right:46px;top:618px;width:300px;text-align:right}

  .contact-title{left:0;width:1062px;top:886px;text-align:center;font-size:16.5px;font-weight:400}
  .contact-row{top:929px;font-size:16px}
  .email{left:294px}
  .phone{left:510px}
  .social{left:702px;top:934px;display:flex;gap:8px}
  .social span{width:13px;height:13px;border-radius:50%;background:var(--ink)}
</style>
</head>
<body>
<main class="site">
  <svg class="shapes" viewBox="0 0 1062 986">
    <defs>
      <linearGradient id="cityTone" x1="0" y1="0" x2="0" y2="1">
        <stop offset="0" stop-color="#7fa9d6"/>
        <stop offset=".3" stop-color="#b9cde0"/>
        <stop offset=".45" stop-color="#a89a78"/>
        <stop offset=".75" stop-color="#6e7a4c"/>
        <stop offset="1" stop-color="#8a6d4f"/>
      </linearGradient>
      <linearGradient id="portraitTone" x1="0" y1="0" x2="1" y2="0">
        <stop offset="0" stop-color="#d7d3c2"/>
        <stop offset=".5" stop-color="#c89a78"/>
        <stop offset="1" stop-color="#a7b08a"/>
      </linearGradient>
    </defs>
    <polygon points="0,0 347,0 402,64 0,64" fill="var(--black)"/>
    <polygon points="347,0 1062,0 1062,64 402,64" fill="var(--gold)"/>
    <polygon points="402,64 1062,64 1062,163 776,502" fill="url(#cityTone)" role="img" aria-label="Aerial photo of a coastal city skyline with a tall communications tower"/>
    <polygon points="95,171 198,261 95,349" fill="var(--pale)"/>
    <rect class="band" x="0" y="518" width="1062" height="337" fill="var(--gold)"/>
    <polygon points="288,775 444,588 610,775" fill="url(#portraitTone)" role="img" aria-label="Portrait photo of a team member"/>
    <polygon points="458,588 774,588 617,775" fill="url(#portraitTone)" role="img" aria-label="Portrait photo of a team member"/>
  </svg>

  <header>
    <div class="abs brand"><span class="brand-name">TALVO</span><span class="brand-mark"></span></div>
    <ul class="abs nav">
      <li>About</li><li>Mission</li><li>Vision</li><li>Values</li><li>Taget Market</li><li>Contact Us</li>
    </ul>
  </header>

  <section class="hero">
    <h1 class="abs hero-title">Talvo Ventures</h1>
    <p class="abs hero-sub">A Kuwait Based Venture Capital</p>
    <p class="abs hero-copy">"Neque porro quisquam est qui dolorem ipsum quia dolor sit amet, consectetur, adipisci velit..." "There is no one who loves pain itself, who seeks after it and wants to have it, simply because it is pain..."  Lorem Ipsum is simply dummy text of the printing and typesetting industry.</p>
    <span class="abs btn">Get Started</span>
  </section>

  <section class="team">
    <div class="member-left">
      <p class="abs member-copy">Lorem Ipsum is simply dummy text of the printing and type setting industry. Lorem Ipsum has been the industry's standard dummy text ever since the 1500s, when an unknown printer took a galley of type and scrambled it to make a type specimen book. It has survived not only five centuries, but also the leap into electronic typesetting, remaining essentially unchanged.</p>
      <h3 class="abs member-name">Rashed Al Qamari</h3>
    </div>
    <div class="member-right">
      <h3 class="abs member-name">Rashed Al Qamari</h3>
      <p class="abs member-copy">Lorem Ipsum is simply dummy text of the printing and type setting industry. Lorem Ipsum has been the industry's standard dummy text ever since the 1500s, when an unknown printer took a galley of type and scrambled it to make a type specimen book. It has survived not only five centuries, but also the leap into electronic typesetting, remaining essentially unchanged.</p>
    </div>
  </section>

  <footer>
    <h2 class="abs contact-title">Get in touch with us!</h2>
    <span class="abs contact-row email">contact@talvo.com</span>
    <span class="abs contact-row phone">+965 5550-1234</span>
    <div class="abs social" aria-label="Social links"><span></span><span></span><span></span></div>
  </footer>
</main>
</body>
</html>
```